Tarvimoor business cards

Need fresh design for our business cards. Logo must be specific, we are open for everything else.

Contact Information for Business Card

phrase "GMP & JANITORIAL SERVICES" should be used as main point of card

Colors
3176b5
3276b5
85acd3
cedeed
ffffff
0292cd
33a6d7
85cae6
cee9f5

Requirements
Must have
• The logo
Should not have
• crowded designs

```html
<!DOCTYPE html>
<html lang="en">
<head>
<meta charset="utf-8">
<title>Tarvimoor Business Cards</title>
<link rel="stylesheet" href="https://fonts.googleapis.com/css2?family=Lato:wght@400;700&display=swap">
<style>
  :root {
    --backdrop: #2b2b2d;
    --card: #1c1d1f;
    --brand-blue: #0292cd;
    --text-light: #c9cacc;
    --text-muted: #a9aaad;
    --rule: #55575b;
    --white: #ffffff;
  }
  * { box-sizing: border-box; margin: 0; padding: 0; }
  html, body { width: 1200px; height: 1108px; overflow: hidden; }
  body {
    background: var(--backdrop);
    font-family: "Lato", Arial, sans-serif;
    position: relative;
  }
  .card {
    position: absolute;
    top: 234px;
    width: 380px;
    height: 640px;
    border-radius: 24px;
    background: var(--card);
    box-shadow: 0 14px 30px rgba(0,0,0,0.45);
    overflow: hidden;
  }
  .card--front { left: 150px; }
  .card--back { left: 670px; }

  .brand-lockup {
    position: absolute; left: 0; right: 0;
    display: flex; flex-direction: column; align-items: center;
  }
  .brand-lockup__inner {
    display: flex; flex-direction: column; align-items: flex-end;
  }
  .brand-name {
    font-family: "Lato", Arial, sans-serif;
    font-weight: 400;
    font-size: 38px;
    line-height: 1;
    letter-spacing: 6px;
    display: flex;
    align-items: center;
    gap: 10px;
    white-space: nowrap;
  }
  .brand-mark { width: 13px; height: 13px; border-radius: 50%; }
  .brand-tagline {
    font-family: "Lato", Arial, sans-serif;
    font-weight: 700;
    font-size: 11px;
    letter-spacing: 2.4px;
    margin-top: 8px;
    white-space: nowrap;
  }

  .card--front .brand-lockup { top: 150px; }
  .card--front .brand-name,
  .card--front .brand-tagline { color: var(--brand-blue); }
  .card--front .brand-mark { background: var(--brand-blue); }

  .card--back .brand-lockup { bottom: 96px; }
  .card--back .brand-name,
  .card--back .brand-tagline { color: var(--white); }
  .card--back .brand-mark { background: var(--white); }

  .contact-block {
    position: absolute; top: 330px; left: 50px; right: 50px;
    text-align: center;
  }
  .person-name {
    color: var(--brand-blue);
    font-size: 24px; font-weight: 400; letter-spacing: 0.5px;
    text-transform: uppercase;
  }
  .person-role { color: var(--text-light); font-size: 19px; margin-top: 2px; }
  .icon-row { display: flex; align-items: center; gap: 6px; margin: 18px 0 14px; }
  .icon-row .rule { flex: 1; height: 1px; background: var(--rule); }
  .icon-badge {
    width: 22px; height: 22px; border-radius: 50%;
    background: var(--brand-blue);
    display: flex; align-items: center; justify-content: center;
  }
  .contact-line { color: var(--text-light); font-size: 20px; line-height: 27px; }
  .divider { height: 1px; background: var(--rule); margin: 14px 0 12px; }
  .address-line { color: var(--text-muted); font-size: 20px; line-height: 27px; }

  .back-texture {
    position: absolute; inset: 0;
    background: linear-gradient(180deg, #252628 0%, #212224 60%, var(--card) 100%);
  }
</style>
</head>
<body>

  <section class="card card--front">
    <div class="brand-lockup">
      <div class="brand-lockup__inner">
        <div class="brand-name"><span>TARVIMOOR</span><span class="brand-mark"></span></div>
        <div class="brand-tagline">GMP &amp; JANITORIAL SERVICES</div>
      </div>
    </div>

    <div class="contact-block">
      <div class="person-name">Daniel Harrow</div>
      <div class="person-role">Managing Director</div>

      <div class="icon-row">
        <span class="rule"></span>
        <span class="icon-badge" aria-label="Phone">
          <svg width="12" height="12" viewBox="0 0 12 12"><path d="M3 1 L5 3.5 L4 5 Q5 7 7 8 L8.5 7 L11 9 L9.5 11 Q4 10.5 1 3 Z" fill="#1c1d1f"/></svg>
        </span>
        <span class="icon-badge" aria-label="Email">
          <svg width="12" height="12" viewBox="0 0 12 12"><rect x="1" y="2.5" width="10" height="7" fill="#1c1d1f"/><path d="M1 2.5 L6 6.5 L11 2.5" stroke="#0292cd" stroke-width="1" fill="none"/></svg>
        </span>
        <span class="icon-badge" aria-label="Website">
          <svg width="12" height="12" viewBox="0 0 12 12"><circle cx="6" cy="6" r="4.8" fill="none" stroke="#1c1d1f" stroke-width="1.3"/><ellipse cx="6" cy="6" rx="2" ry="4.8" fill="none" stroke="#1c1d1f" stroke-width="1"/><line x1="1.2" y1="6" x2="10.8" y2="6" stroke="#1c1d1f" stroke-width="1"/></svg>
        </span>
        <span class="rule"></span>
      </div>

      <div class="contact-line">444 555 1270</div>
      <div class="contact-line">hello@tarvimoor.com</div>
      <div class="contact-line">www.tarvimoor.com</div>

      <div class="divider"></div>

      <div class="address-line">421, Address line here,</div>
      <div class="address-line">Country Name, 45452</div>
    </div>
  </section>

  <section class="card card--back">
    <div class="back-texture" role="img" aria-label="Faint repeating circle pattern in dark grey"></div>
    <div class="brand-lockup">
      <div class="brand-lockup__inner">
        <div class="brand-name"><span>TARVIMOOR</span><span class="brand-mark"></span></div>
        <div class="brand-tagline">GMP &amp; JANITORIAL SERVICES</div>
      </div>
    </div>
  </section>

</body>
</html>
```